Travel Agency Website - Simple General

Need a 7 page simple design that is pretty repetitive. Need to be able to load quickly that is SEO optimized. Trying to give ideas on what they can do, be personal as we are local, but at the same time come across as professional and get information easily with little burden.

- Landing Page
- Brambleton Vacations Page
- Family Trips
- Road Trips from Texas
- Other Destinations
- About Us Page
- Contact Us Page

Target Market(s)

Families

Coding

Coded - Design and coding required

Number of Pages Required

5+ page

Colors

Designer to choose colors to be used in the design.

Requirements
Must have
• Like it to flow easily with our logo. Use that for colors, etc.

```html
<!DOCTYPE html>
<html lang="en">
<head>
<meta charset="utf-8">
<title>Wandering Finch Travel – Your Local Guide to Big Adventure</title>
<link href="https://fonts.googleapis.com/css2?family=Inter:wght@400;500;700&display=swap" rel="stylesheet">
<style>
:root{
  --teal:#2f8080;
  --teal-dark:#1f5a66;
  --gold:#a07a38;
  --ink:#1b1b1b;
  --muted:#666a6d;
  --sky-tint:#e8f5f9;
  --cream-tint:#fdf8e8;
  --white:#ffffff;
  --rule:#dcdcdc;
}
*{box-sizing:border-box;margin:0;padding:0}
html,body{width:695px;height:1200px;overflow:hidden;background:var(--white)}
body{position:relative;font-family:"Inter",Arial,sans-serif;color:var(--ink)}
.abs{position:absolute}
.backdrop{position:absolute;left:0;top:0;width:695px;height:600px;pointer-events:none}
.brand{left:10px;top:8px;width:74px;height:56px;display:flex;align-items:center;gap:4px;color:var(--teal-dark);font-size:10px;font-weight:700;line-height:1.1}
.brand i{display:block;width:9px;height:9px;border-radius:50%;background:var(--teal);flex:none}
.main-nav{left:152px;top:22px;width:533px;height:30px;background:var(--teal);border-radius:5px;display:flex;align-items:center;justify-content:center;gap:18px}
.main-nav a{color:var(--white);font-size:7.6px;font-weight:500;text-decoration:none;position:relative}
.main-nav a.current::after{content:"";position:absolute;left:50%;bottom:-8px;margin-left:-3px;border:3px solid transparent;border-bottom-color:var(--teal-dark)}
.hero{left:12.5px;top:73px;width:672.5px;height:276px;border-radius:9px;overflow:hidden}
.hero-photo{position:absolute;inset:0;background:linear-gradient(100deg,#8d9a9d 0%,#b9c4c6 30%,#d3d7d6 55%,#a9b2b0 80%,#7e8a86 100%)}
.hero-cloud{position:absolute;left:110px;top:170px;width:480px;height:110px;border-radius:50%;background:radial-gradient(ellipse at center,rgba(255,255,255,.92) 55%,rgba(255,255,255,0) 72%)}
.hero-title{position:absolute;left:0;right:0;top:196px;text-align:center;color:var(--teal-dark);font-size:23px;font-weight:400;line-height:28px}
.hero-title b{color:var(--gold);font-weight:700}
.hero-arrow{position:absolute;top:128px;width:21px;height:21px}
.hero-dots{position:absolute;left:327px;top:264px;display:flex;gap:4px}
.hero-dots span{width:4px;height:4px;border-radius:50%;background:var(--white)}
.tagline{left:292px;top:401px;width:182px;height:18px;background:rgba(255,255,255,.6);border:1px solid #d6ecf1;border-radius:3px}
.tagline-text{left:0;width:695px;top:405px;text-align:center;color:var(--teal-dark);font-size:9.5px;font-weight:500}
.intro{left:109px;top:434px;width:480px;font-size:7.6px;line-height:11.6px}
.intro p{margin-bottom:11.5px}
.offer h2{font-size:8.7px;font-weight:500;color:var(--teal-dark);margin-bottom:5px}
.offer h2.dark{color:var(--ink)}
.offer .sub{font-size:7px;font-weight:500;margin:-4px 0 6px}
.offer p{font-size:7.6px;line-height:9.2px;color:#2a2a2a}
.photo{border-radius:5px}
.site-footer{left:0;top:1092px;width:695px;height:100px;border-top:1px solid var(--rule)}
.foot-brand{left:20px;top:1115px;width:66px;height:44px;display:flex;align-items:center;gap:4px;color:var(--teal-dark);font-size:10px;font-weight:700;line-height:1.1}
.foot-brand i{display:block;width:9px;height:9px;border-radius:50%;background:var(--teal);flex:none}
.foot-links{font-size:7.7px;color:var(--muted);line-height:16.5px;list-style:none}
.social{left:476px;top:1141px;display:flex;gap:8px}
.social span{width:11px;height:11px;border:1.3px solid #8a8a8a;border-radius:3px}
.bottom-band{left:0;top:1192px;width:695px;height:8px;background:#dedede}
</style>
</head>
<body>
<svg class="backdrop" viewBox="0 0 695 600" aria-hidden="true">
  <circle cx="60" cy="420" r="200" fill="var(--sky-tint)"/>
  <ellipse cx="190" cy="420" rx="65" ry="150" fill="var(--cream-tint)"/>
  <circle cx="20" cy="300" r="55" fill="var(--cream-tint)"/>
</svg>

<header>
  <div class="abs brand"><i></i><span>Wandering Finch</span></div>
  <nav class="abs main-nav">
    <a class="current" href="#">Home</a>
    <a href="#">Brambleton Vacations</a>
    <a href="#">Family Trips</a>
    <a href="#">Road Trips from Texas</a>
    <a href="#">Other Destinations</a>
    <a href="#">About Us</a>
    <a href="#">Contact Us</a>
  </nav>
</header>

<section class="abs hero">
  <div class="hero-photo" role="img" aria-label="Three friends reading a map beside an off-road vehicle on a country track"></div>
  <div class="hero-cloud"></div>
  <h1 class="hero-title">Wandering Finch Travel<br>Your local Guide to <b>Big Adventure</b></h1>
  <svg class="hero-arrow" style="left:10px" viewBox="0 0 22 22" aria-hidden="true"><circle cx="11" cy="11" r="10" fill="none" stroke="#e8eeee" stroke-width="1.5"/><path d="M15 11H7M10.5 7.5 7 11l3.5 3.5" fill="none" stroke="#e8eeee" stroke-width="1.5"/></svg>
  <svg class="hero-arrow" style="left:641px" viewBox="0 0 22 22" aria-hidden="true"><circle cx="11" cy="11" r="10" fill="none" stroke="#e8eeee" stroke-width="1.5"/><path d="M7 11h8M11.5 7.5 15 11l-3.5 3.5" fill="none" stroke="#e8eeee" stroke-width="1.5"/></svg>
  <div class="hero-dots"><span></span><span></span><span></span></div>
</section>

<div class="abs tagline"></div>
<h2 class="abs tagline-text">No stress. No confusion. Just smooth</h2>

<section class="abs intro">
  <p>Turn your travel dreams into seamless, unforgettable experiences. At <b>Wandering Finch Travel</b>, we believe planning your trip should feel just as exciting as the journey itself not overwhelming.</p>
  <p>From magical theme park adventures and relaxing beach escapes to scenic road trips and hidden destination gems, we take care of every detail so you can focus on making memories. Whether you're traveling with family, friends, or planning a solo escape, we create personalized itineraries tailored to your style, budget, and pace.</p>
  <p><b>No stress. No confusion. Just smooth</b>, well-planned travel from start to finish.</p>
</section>

<article class="abs offer" style="left:88px;top:571px;width:256px">
  <h2>Brambleton Vacations – Land and Sea</h2>
  <p>Experience the magic on land and cruise the seas with perfectly planned Brambleton adventures.</p>
</article>
<div class="abs photo" style="left:88px;top:614px;width:256px;height:169px;background:linear-gradient(180deg,#3f8ee0 0%,#6fb2ee 45%,#5a7a4a 65%,#8a6a5a 100%)" role="img" aria-label="Crowds walking through a theme park entrance gate under blue sky"></div>

<article class="abs offer" style="left:360px;top:571px;width:256px">
  <h2>Family Trips</h2>
  <p>Create lifelong memories with customized trips designed for all ages.</p>
</article>
<div class="abs photo" style="left:359px;top:615px;width:255px;height:170px;background:linear-gradient(120deg,#8fb36a 0%,#d9e6d2 40%,#bfd8e0 70%,#6f9f6a 100%)" role="img" aria-label="Family with suitcases arriving at a sunny resort with palm trees"></div>

<article class="abs offer" style="left:88px;top:816px;width:256px">
  <h2 class="dark">Texas Road Trips</h2>
  <div class="sub">(Partnership with Piney Road Van Rentals)</div>
  <p>Hit the road and explore Texas with flexible, fun, and comfortable van travel.</p>
</article>
<div class="abs photo" style="left:88px;top:867px;width:256px;height:171px;background:linear-gradient(180deg,#7fb9e6 0%,#e8d3b0 35%,#c98a5a 60%,#6d6a6a 100%)" role="img" aria-label="Aerial view of a Texas city skyline and highways at sunset"></div>

<article class="abs offer" style="left:359px;top:815px;width:256px">
  <h2 class="dark">Other Destinations</h2>
  <p>Discover unique destinations worldwide tailored to your travel dreams.</p>
</article>
<div class="abs photo" style="left:359px;top:866px;width:255px;height:172px;background:linear-gradient(180deg,#7cc3f2 0%,#9fd2f4 55%,#5d9a5a 80%,#b5262e 100%)" role="img" aria-label="Hand holding a red suitcase with a straw hat, airplane in blue sky"></div>

<footer class="abs site-footer"></footer>
<div class="abs foot-brand"><i></i><span>Wandering Finch</span></div>
<ul class="abs foot-links" style="left:144px;top:1105px">
  <li>Home</li><li>About Us</li><li>Contact Us</li>
</ul>
<ul class="abs foot-links" style="left:298px;top:1105px">
  <li>Brambleton Vacations</li><li>Family Trips</li><li>Road Trips from Texas</li><li>Other Destinations</li>
</ul>
<ul class="abs foot-links" style="left:476px;top:1105px">
  <li>hello@wanderingfinchtravel.com</li><li>01 - 111111111111</li>
</ul>
<div class="abs social" aria-label="Social links"><span></span><span></span><span></span></div>
<div class="abs bottom-band"></div>
</body>
</html>
```